Empower our Electric Journey on the Web

We need a new website that can promote our services. Our three services that we offer are:
- Management of e-mobility charging stations
- Management of energy purchases
- Leasing of E-Mobility charging stations
- Energy billing of private electricity meters
The website should work responsively on PC, tablet and smartphone. In general, a simple navigation and an appealing design should be in the foreground. The website should give the customer the possibility to request , based pm a preset chexkbox chart and to get in contact with us.
Our logo works on black and white background.
Our slogan is:
Empower Your Electric Journey with Velmor Mobility
The 4 Pages should be the following:
Main Page, with info about us, why choose us,
2nd; services; what we sell and what are our services
3rd; Contact us, request an offer
4th, References about costumers and Work we already did, in the future we would like to integrate a Blog Post in this section in stead of references.

Target Market(s)

Landlords, Homeowners, Homeowner Associations

Industry/Entity Type

EV Chargers / E-Mobility

Coding

Coded - Design and coding required

Number of Pages Required

4 page

Requirements
Nice to have
• Pop up to our mailchimp newsletter subscription

```html
<!DOCTYPE html>
<html lang="en">
<head>
<meta charset="utf-8">
<title>Velmor Mobility</title>
<link href="https://fonts.googleapis.com/css2?family=Rajdhani:wght@600;700&family=Lato:wght@400;700&display=swap" rel="stylesheet">
<style>
:root{
  --green:#5fcf3c;
  --green-light:#8ce646;
  --green-dark:#36b04a;
  --ink:#1c1c1c;
  --dark:#1f1d1e;
  --text:#4a4a4a;
  --muted:#8a8a8a;
  --line:#cfcfcf;
  --white:#fff;
  --star:#f2a81d;
}
*{box-sizing:border-box;margin:0;padding:0}
html,body{width:1200px;height:3845px;overflow:hidden}
body{position:relative;background:var(--white);font-family:'Lato',sans-serif;color:var(--text)}
.abs{position:absolute}
.head{font-family:'Rajdhani',sans-serif;font-weight:700;color:var(--ink);line-height:1.2}
.label{font-family:'Rajdhani',sans-serif;font-weight:600;color:var(--green);font-size:15px;text-transform:uppercase;letter-spacing:.3px}
.photo{position:absolute;overflow:hidden}
.btn{position:absolute;display:flex;align-items:center;justify-content:space-between;border-radius:30px;background:linear-gradient(90deg,var(--green-light),var(--green-dark));color:#fff;font-weight:700;font-size:16px;padding:0 5px 0 32px}
.btn .arrow{width:36px;height:36px;border-radius:50%;background:#fff;display:flex;align-items:center;justify-content:center}
.brand{position:absolute;display:flex;align-items:center;gap:10px;font-family:'Rajdhani',sans-serif;font-weight:700;font-size:26px;letter-spacing:2px;text-transform:uppercase}
.brand .mark{width:18px;height:18px;background:var(--green)}

/* nav */
.nav{position:absolute;top:35px;left:355px;display:flex;gap:27px;font-size:16px;color:var(--ink)}
.nav a{text-decoration:none;color:inherit}
.nav .active{color:var(--green)}
.nav-phone{left:937px;top:25px;width:178px;height:45px;padding:0 0 0 4px;justify-content:flex-start;gap:14px;font-size:16px}

/* hero */
.hero{left:0;top:0;width:1200px;height:642px;background:linear-gradient(180deg,#e6e7e9 0%,#eeeff0 70%,#fff 100%)}
.hero-accent{left:75px;top:112px;width:630px;height:466px;border-radius:8px;background:radial-gradient(ellipse at 50% 50%,rgba(95,207,60,.55) 0%,rgba(95,207,60,.22) 55%,rgba(95,207,60,0) 75%)}
.hero-eyebrow{left:637px;top:258px;font-family:'Rajdhani',sans-serif;font-weight:600;font-size:21px;letter-spacing:6px;color:var(--green)}
.hero-title{left:637px;top:290px;font-size:51px;line-height:61px;text-transform:uppercase;letter-spacing:.5px}

/* about */
.about-photo{left:161px;top:719px;width:391px;height:460px;border-radius:24px;background:linear-gradient(160deg,#5e87c4 0%,#9cb7d8 40%,#5a5254 70%,#d9d9d9 100%)}
.about-inset{left:85px;top:878px;width:142px;height:142px;border-radius:50%;border:5px solid var(--green);background:linear-gradient(135deg,#9aa39a,#4b4b4b)}
.badge{left:467px;top:791px;width:137px;height:58px;background:#fff;border-radius:6px;box-shadow:0 4px 14px rgba(0,0,0,.12);display:flex;align-items:center;gap:6px;padding-left:9px}
.badge b{font-family:'Rajdhani',sans-serif;font-size:25px;color:var(--green)}
.badge span{font-size:14px;line-height:17px;color:var(--ink)}
.soft-ring{border-radius:50%;background:radial-gradient(circle,rgba(95,207,60,.25),rgba(95,207,60,.08))}
.section-title{font-size:40px;line-height:48px}
.body-copy{font-size:13.6px;line-height:24px}
.query{position:absolute;left:880px;top:1062px;display:flex;gap:12px;align-items:center}
.query p{font-size:14px;font-weight:700;color:var(--ink);line-height:22px}

/* why */
.why{left:0;top:1257px;width:1200px;height:542px;background:var(--dark)}
.why-band{left:928px;top:1257px;width:272px;height:486px;background:linear-gradient(160deg,var(--green-light),var(--green-dark))}
.why-photo{left:589px;top:1325px;width:481px;height:384px;border-radius:18px;background:linear-gradient(135deg,#8a8a8a 0%,#5b5e63 45%,#bfc2c6 75%,#e9e9e9 100%)}
.why .head{color:#fff}
.ticks{list-style:none}
.ticks li{display:flex;align-items:center;gap:10px;color:#fff;font-weight:700;font-size:14px;height:42px}

/* services */
.service-card{position:absolute;top:1942px;width:331px}
.service-card .photo{position:relative;width:331px;height:213px;border-radius:6px}
.plus{position:absolute;top:197px;right:24px;width:34px;height:34px;border-radius:50%;background:var(--green);color:#fff;font-size:24px;display:flex;align-items:center;justify-content:center}
.service-card h3{font-family:'Rajdhani',sans-serif;font-weight:600;font-size:20px;line-height:26px;color:var(--ink);margin-top:26px}
.service-card p{font-size:13px;line-height:22px;margin-top:6px}

/* testimonials */
.reviews{left:0;top:2366px;width:1200px;height:503px;background:linear-gradient(135deg,#262425,#1a1819)}
.review{position:absolute;top:2530px;width:323px;height:252px;background:#fff;border-radius:8px;padding:22px 17px}
.review .who{display:flex;align-items:center;gap:10px}
.avatar{width:56px;height:56px;border-radius:50%;background:linear-gradient(135deg,#d7dbe0,#8f98a3)}
.who h4{font-family:'Rajdhani',sans-serif;font-weight:700;font-size:19px;color:var(--green);line-height:20px}
.who span{font-size:14px;color:var(--muted)}
.review p{font-size:13.6px;line-height:22px;margin-top:16px;padding-bottom:16px;border-bottom:1px solid var(--line)}
.stars{color:var(--star);font-size:17px;letter-spacing:2px;margin-top:10px}
.chev{position:absolute;top:2662px;color:#bbb;font-size:24px}

/* contact */
.field{position:absolute;border:1px solid #bdbdbd;font-size:14px;color:var(--ink);padding:14px}
.contact-photo{left:722px;top:2949px;width:393px;height:376px;border-radius:30px 0 24px 24px;background:linear-gradient(135deg,#4a3f3a 0%,#7d6a5c 45%,#e6e4e2 60%,#9a8c80 100%)}
.green-block{left:767px;top:2916px;width:72px;height:72px;background:linear-gradient(135deg,var(--green-light),var(--green-dark))}

/* footer */
.footer{left:0;top:3395px;width:1200px;height:450px;background:var(--dark);color:#d5d5d5}
.footer h5{position:absolute;top:3462px;font-family:'Rajdhani',sans-serif;font-weight:700;font-size:19px;color:#fff}
.flinks{position:absolute;list-style:none;font-size:15px;color:#cfcfcf}
.flinks li{position:relative;padding-left:18px}
.flinks li::before{content:"›";position:absolute;left:0;top:-1px;color:var(--green);font-size:17px}
.contact-row{position:absolute;left:85px;display:flex;align-items:center;gap:14px;font-size:15px;color:#e6e6e6}
.social{position:absolute;top:3655px;width:30px;height:30px;border-radius:50%;background:#fff}
.sub-input{left:870px;top:3567px;width:243px;height:42px;background:#fff;border-radius:22px;display:flex;align-items:center;gap:8px;padding-left:16px;font-size:13px;color:var(--muted)}
.rule{left:85px;top:3769px;width:1030px;height:1px;background:#3d3b3c}
</style>
</head>
<body>

<!-- HERO -->
<div class="photo hero abs" role="img" aria-label="Man charging a white electric car at a home charging station"></div>
<div class="abs hero-accent" role="img" aria-label="Decorative green angular shapes"></div>
<div class="brand" style="left:85px;top:29px;color:var(--ink)"><span class="mark"></span>Velmor Mobility</div>
<nav class="nav">
  <a class="active">HOME</a><a>ABOUT US</a><a>WHY CHOOSE US</a><a>SERVICES</a><a>CONTACT US</a>
</nav>
<div class="btn nav-phone">
  <span class="arrow"><svg width="18" height="18" viewBox="0 0 24 24"><path d="M6.6 10.8a15 15 0 0 0 6.6 6.6l2.2-2.2a1 1 0 0 1 1-.25 11.4 11.4 0 0 0 3.6.6 1 1 0 0 1 1 1V20a1 1 0 0 1-1 1A17 17 0 0 1 3 4a1 1 0 0 1 1-1h3.5a1 1 0 0 1 1 1 11.4 11.4 0 0 0 .6 3.6 1 1 0 0 1-.25 1z" fill="#3fba48"/></svg></span>555 210 3390
</div>
<div class="abs hero-eyebrow">EMPOWER YOUR</div>
<h1 class="abs head hero-title">Electric Journey<br>with Velmor Mobility</h1>

<!-- ABOUT -->
<div class="photo about-photo" role="img" aria-label="Woman standing beside an electric car charging outside a modern house"></div>
<div class="photo about-inset" role="img" aria-label="Close-up of a hand plugging in a charging connector"></div>
<div class="abs badge"><b>35+</b><span>Years of<br>Experience</span></div>
<div class="abs soft-ring" style="left:522px;top:1142px;width:68px;height:70px"></div>
<div class="abs label" style="left:655px;top:764px">About Velmor Mobility</div>
<h2 class="abs head section-title" style="left:655px;top:785px;width:470px">Professional Electric Vehicle Charging Solution For You</h2>
<p class="abs body-copy" style="left:655px;top:891px;width:462px">Lorem ipsum dolor sit amet, conseur adipiscing elit, sed do eiusmod tempor incididunt ut labore et dolo aliqua. Quis ipsum suspendisse ultrices gravida. Risus commodo vi maecenaan lacus vel facilisis. Duis sed sodales mauris, id ementum ex. Sed cursus iaculis libero in lobortis. Aenean consectetur elit sed turpis sodalessan. Aliquam erat volutpat. Suspendisse aliquam sa feugiat enim elementum id.</p>
<div class="btn" style="left:655px;top:1063px;width:180px;height:45px">Read More<span class="arrow"><svg width="16" height="12" viewBox="0 0 16 12"><path d="M1 9 C4 3 9 3 14 6 M10 2 L14 6 L10 10" fill="none" stroke="#3fba48" stroke-width="1.6"/></svg></span></div>
<div class="query">
  <svg width="22" height="24" viewBox="0 0 24 24"><path d="M6.6 10.8a15 15 0 0 0 6.6 6.6l2.2-2.2a1 1 0 0 1 1-.25 11.4 11.4 0 0 0 3.6.6 1 1 0 0 1 1 1V20a1 1 0 0 1-1 1A17 17 0 0 1 3 4a1 1 0 0 1 1-1h3.5a1 1 0 0 1 1 1 11.4 11.4 0 0 0 .6 3.6 1 1 0 0 1-.25 1z" fill="#3fba48"/></svg>
  <p>Any Quary?<br>+1 555 210 3390</p>
</div>

<!-- WHY CHOOSE US -->
<section class="abs why">
  <div class="abs label" style="left:85px;top:89px">Why Choose Us</div>
  <h2 class="abs head" style="left:85px;top:110px;font-size:38px;line-height:44px">Take Care of Your Car<br>&amp; Our Planet</h2>
  <p class="abs body-copy" style="left:85px;top:205px;width:420px;color:#e4e4e4">Donec lacinia porta urna, eget convallis magna posuere et. Proin iaculis feugiat eleifend. Sed quis lacus eget sapien fringilla ultricies sit amet nec dolor. Nulla facilisi. Donec efficitur accumsan odio. Nam tempor sollicitudin posuere</p>
  <ul class="abs ticks" style="left:85px;top:316px">
    <li><svg width="16" height="16" viewBox="0 0 16 16"><circle cx="8" cy="8" r="8" fill="#5fcf3c"/><path d="M4.5 8.2l2.3 2.2 4.7-4.7" fill="none" stroke="#fff" stroke-width="1.8"/></svg>2 or 3 year warranty, extendable to 5 years</li>
    <li><svg width="16" height="16" viewBox="0 0 16 16"><circle cx="8" cy="8" r="8" fill="#5fcf3c"/><path d="M4.5 8.2l2.3 2.2 4.7-4.7" fill="none" stroke="#fff" stroke-width="1.8"/></svg>Monitor your charging and earn rewards by charging</li>
    <li><svg width="16" height="16" viewBox="0 0 16 16"><circle cx="8" cy="8" r="8" fill="#5fcf3c"/><path d="M4.5 8.2l2.3 2.2 4.7-4.7" fill="none" stroke="#fff" stroke-width="1.8"/></svg>Hundreds of thousands of places to charge</li>
  </ul>
</section>
<div class="abs why-band"></div>
<div class="photo why-photo" role="img" aria-label="Family near a wall-mounted charger with a white electric car plugged in"></div>
<div class="abs soft-ring" style="left:569px;top:1682px;width:70px;height:70px"></div>

<!-- SERVICES -->
<div class="abs label" style="left:0;width:1200px;text-align:center;top:1855px">Our Services</div>
<h2 class="abs head section-title" style="left:0;width:1200px;text-align:center;top:1877px">Best Charging Services For Your EV</h2>
<div class="service-card" style="left:85px">
  <div class="photo" role="img" aria-label="Woman beside a white electric car at a garage charger" style="background:linear-gradient(135deg,#5c5e62,#bfc1c4 60%,#eee)"></div>
  <span class="plus">+</span>
  <h3>Management of e-mobility charging stations</h3>
  <p>Lorem ipsum dolor sit amet, coectetur adipiscing elit. Nullam venenatis rutrum velit sit amet cursus. Curabitur nec enim ex.</p>
</div>
<div class="service-card" style="left:434px">
  <div class="photo" role="img" aria-label="White electric car charging while a man checks his phone" style="background:linear-gradient(135deg,#7b7267,#d8d6d2 55%,#6b6f74)"></div>
  <span class="plus">+</span>
  <h3>Management of energy purchases</h3>
  <p>Lorem ipsum dolor sit amet, coectetur adipiscing elit. Nullam venenatis rutrum velit sit amet cursus. Curabitur nec enim ex.</p>
</div>
<div class="service-card" style="left:784px">
  <div class="photo" role="img" aria-label="Man plugging a charging cable into an electric car" style="background:linear-gradient(135deg,#2f3338,#8a8f96 50%,#d4d4d4)"></div>
  <span class="plus">+</span>
  <h3>Leasing of E-Mobility charging stations</h3>
  <p>Lorem ipsum dolor sit amet, coectetur adipiscing elit. Nullam venenatis rutrum velit sit amet cursus. Curabitur nec enim ex.</p>
</div>

<!-- TESTIMONIALS -->
<div class="abs reviews"></div>
<div class="abs label" style="left:0;width:1200px;text-align:center;top:2442px">Testimonials</div>
<h2 class="abs head section-title" style="left:0;width:1200px;text-align:center;top:2465px;color:#fff">Our Clients Says</h2>
<span class="chev" style="left:72px">‹</span><span class="chev" style="left:1113px">›</span>
<div class="review" style="left:85px">
  <div class="who"><div class="avatar" role="img" aria-label="Customer portrait"></div><div><h4>Miren Adebayo</h4><span>Customer</span></div></div>
  <p>Coectetur adipiscing elit. Nullam venenatis rutrum velit sit amet cursus. Curabitur nec enim exurna quis fringillaconsequat. Donec dolor erat, lobortis sit amet iaculis at.</p>
  <div class="stars">★★★★★</div>
</div>
<div class="review" style="left:439px">
  <div class="who"><div class="avatar" role="img" aria-label="Customer portrait"></div><div><h4>Miren Adebayo</h4><span>Customer</span></div></div>
  <p>Coectetur adipiscing elit. Nullam venenatis rutrum velit sit amet cursus. Curabitur nec enim exurna quis fringillaconsequat. Donec dolor erat, lobortis sit amet iaculis at.</p>
  <div class="stars">★★★★★</div>
</div>
<div class="review" style="left:791px">
  <div class="who"><div class="avatar" role="img" aria-label="Customer portrait"></div><div><h4>Miren Adebayo</h4><span>Customer</span></div></div>
  <p>Coectetur adipiscing elit. Nullam venenatis rutrum velit sit amet cursus. Curabitur nec enim exurna quis fringillaconsequat. Donec dolor erat, lobortis sit amet iaculis at.</p>
  <div class="stars">★★★★★</div>
</div>

<!-- CONTACT -->
<div class="abs label" style="left:85px;top:2958px">Contact Us</div>
<h2 class="abs head section-title" style="left:85px;top:2978px">Get In Touch</h2>
<div class="field" style="left:85px;top:3039px;width:301px;height:47px">First Name</div>
<div class="field" style="left:394px;top:3039px;width:301px;height:47px">Last Name</div>
<div class="field" style="left:85px;top:3095px;width:301px;height:48px">Email</div>
<div class="field" style="left:394px;top:3095px;width:301px;height:48px">Phone</div>
<div class="field" style="left:85px;top:3154px;width:610px;height:114px">Your Message</div>
<div class="btn" style="left:85px;top:3290px;width:214px;height:44px;padding-left:28px">Submit Request<span class="arrow"><svg width="16" height="12" viewBox="0 0 16 12"><path d="M1 9 C4 3 9 3 14 6 M10 2 L14 6 L10 10" fill="none" stroke="#3fba48" stroke-width="1.6"/></svg></span></div>
<div class="photo contact-photo" role="img" aria-label="Man plugging a charger into a white car"></div>
<div class="abs green-block"></div>
<div class="abs soft-ring" style="left:701px;top:3283px;width:75px;height:75px"></div>

<!-- FOOTER -->
<footer class="abs footer"></footer>
<div class="brand" style="left:85px;top:3473px;color:#fff"><span class="mark"></span>Velmor Mobility</div>
<div class="contact-row" style="top:3548px"><svg width="18" height="14" viewBox="0 0 18 14"><rect width="18" height="14" rx="2" fill="#5fcf3c"/><path d="M1 2l8 6 8-6" fill="none" stroke="#1f1d1e" stroke-width="1.5"/></svg>hello@velmormobility.com</div>
<div class="contact-row" style="top:3591px"><svg width="18" height="18" viewBox="0 0 24 24"><path d="M6.6 10.8a15 15 0 0 0 6.6 6.6l2.2-2.2a1 1 0 0 1 1-.25 11.4 11.4 0 0 0 3.6.6 1 1 0 0 1 1 1V20a1 1 0 0 1-1 1A17 17 0 0 1 3 4a1 1 0 0 1 1-1h3.5a1 1 0 0 1 1 1 11.4 11.4 0 0 0 .6 3.6 1 1 0 0 1-.25 1z" fill="#5fcf3c"/></svg>+1555 210 3390</div>
<span class="social" style="left:85px" aria-label="Social link"></span>
<span class="social" style="left:131px" aria-label="Social link"></span>
<span class="social" style="left:178px" aria-label="Social link"></span>
<span class="social" style="left:225px" aria-label="Social link"></span>

<h5 style="left:372px">Quick Links</h5>
<ul class="flinks" style="left:372px;top:3512px;line-height:43px">
  <li>Home</li><li>About Us</li><li>Why Choose Us</li><li>Services</li><li>Contact Us</li>
</ul>
<h5 style="left:560px">Services</h5>
<ul class="flinks" style="left:560px;top:3512px;width:270px;line-height:25px">
  <li style="margin-bottom:12px">Management of e-mobility charging stations</li>
  <li style="margin-bottom:12px">Management of energy purchases</li>
  <li style="margin-bottom:12px">Leasing of E-Mobility charging stations</li>
  <li>Energy billing of private electricity meters</li>
</ul>
<h5 style="left:870px">Newsletter</h5>
<div class="abs" style="left:870px;top:3492px;width:60px;height:2px;background:var(--green)"></div>
<p class="abs" style="left:870px;top:3503px;width:230px;font-size:15px;line-height:29px;color:#cfcfcf">Subscribe For The Our Latest Updates !</p>
<div class="abs sub-input"><svg width="14" height="11" viewBox="0 0 18 14"><rect width="18" height="14" rx="2" fill="#9a9a9a"/><path d="M1 2l8 6 8-6" fill="none" stroke="#fff" stroke-width="1.5"/></svg>Subscribe with us</div>
<div class="btn" style="left:873px;top:3619px;width:240px;height:44px;padding-left:60px">Subscribe<span class="arrow"><svg width="16" height="12" viewBox="0 0 16 12"><path d="M1 9 C4 3 9 3 14 6 M10 2 L14 6 L10 10" fill="none" stroke="#3fba48" stroke-width="1.6"/></svg></span></div>
<div class="abs rule"></div>
<p class="abs" style="left:85px;top:3795px;font-size:14px;color:#e0e0e0">© 2023 <span style="color:var(--green)">VELMOR MOBILITY</span>. All right reserved</p>

</body>
</html>
```